Aerial photo/video drone company needs new business card

Aerial visual company who offers photos and video services via drones.

We are KTO certified and work in the real estate, insurance, construction, and film industries.

I'm looking for a clean, professional, maybe even edgy design, that will be a conversation starter when networking.

I've included our logo, current business card, and font.

Our current business card is decent; albeit, I'm looking for something more unique. If you folks provide good designs, I'll definitely guarantee payment (and I'm not opposed to tipping if the design is above and beyond).

Target Market(s)

Insurance companies, real estate agents, construction companies, advertising & other creative agencies, and filmmakers/producers.

Industry/Entity Type

Business

Contact Information for Business Card

Company name pronounced tol-u-mo.

Other font styles liked:
• Font was uploaded; that or similar; not opposed to other fonts if they work well with the design

Requirements
Must have
• Clearly prominent logo; my name and title; phone number; email address; web address; mentioned "KTO Certified" or similar; should indicate "Aerial visual"
Nice to have
• Watermark of logo or otherwise
Should not have
• Pictures of drones or scenic shots

```html
<!DOCTYPE html>
<html lang="en">
<head>
<meta charset="utf-8">
<title>Tolumo business card</title>
<link rel="stylesheet" href="https://fonts.googleapis.com/css2?family=Montserrat:wght@600&family=Source+Sans+3:wght@400;600&display=swap">
<style>
  :root {
    --stage: #000000;
    --navy: #263a5a;
    --sky: #0596db;
    --white: #ffffff;
    --card-radius: 46px;
  }
  html, body {
    margin: 0;
    padding: 0;
    width: 1200px;
    height: 900px;
    overflow: hidden;
    background: var(--stage);
  }
  .canvas {
    position: relative;
    width: 1200px;
    height: 900px;
    font-family: "Source Sans 3", "Myriad Pro", sans-serif;
  }
  .card {
    position: absolute;
    top: 275px;
    width: 477px;
    height: 293px;
    box-sizing: border-box;
  }
  .card-front {
    left: 116px;
    background: var(--navy);
    border-radius: 0 var(--card-radius) 0 var(--card-radius);
    color: var(--white);
  }
  .card-back {
    left: 622px;
    background: var(--sky);
    border-radius: var(--card-radius) 0 var(--card-radius) 0;
  }
  .holder {
    position: absolute;
    left: 25px;
    top: 42px;
  }
  .holder-name {
    margin: 0;
    font-size: 17px;
    font-weight: 600;
    color: var(--sky);
    line-height: 22px;
  }
  .holder-title {
    margin: 0;
    font-size: 13px;
    line-height: 18px;
  }
  .contacts {
    position: absolute;
    right: 22px;
    top: 33px;
    margin: 0;
    padding: 0;
    list-style: none;
    text-align: right;
    font-size: 13px;
    line-height: 19.5px;
  }
  .contacts li {
    display: flex;
    justify-content: flex-end;
    align-items: center;
    gap: 6px;
  }
  .contacts svg { width: 10px; height: 10px; fill: var(--sky); }
  .brand {
    position: absolute;
    left: 0;
    right: 0;
    text-align: center;
    font-family: "Montserrat", sans-serif;
    font-weight: 600;
    letter-spacing: 1px;
    line-height: 1;
  }
  .brand-dot {
    display: block;
    margin: 0 auto;
    border-radius: 50%;
  }
  .card-front .brand { top: 78px; color: var(--white); font-size: 56px; }
  .card-front .brand-dot { width: 46px; height: 46px; background: var(--sky); margin-bottom: 14px; }
  .card-back .brand { top: 78px; color: var(--navy); font-size: 68px; }
  .card-back .brand-dot { width: 60px; height: 60px; background: var(--navy); margin-bottom: 18px; }
  .divider {
    position: absolute;
    left: 0;
    right: 0;
    top: 213px;
    height: 1.5px;
    background: var(--sky);
  }
  .services {
    position: absolute;
    left: 0;
    right: 0;
    top: 230px;
    margin: 0;
    text-align: center;
    font-size: 13.5px;
  }
  .certification {
    position: absolute;
    left: 0;
    right: 0;
    top: 260px;
    margin: 0;
    text-align: center;
    font-size: 13px;
    font-weight: 600;
    color: var(--sky);
  }
</style>
</head>
<body>
<main class="canvas">
  <section class="card card-front">
    <div class="holder">
      <p class="holder-name">Daniel K.Ferrow</p>
      <p class="holder-title">Owner . sUAS Pilot</p>
    </div>
    <ul class="contacts">
      <li>555.014.2273
        <svg viewBox="0 0 10 10" aria-hidden="true"><path d="M2 0.5 L3.6 2.6 L2.8 3.6 Q4 6 6.4 7.2 L7.4 6.4 L9.5 8 L8.4 9.5 Q3.8 9 0.5 1.6 Z"/></svg>
      </li>
      <li>dan@tolumo.com
        <svg viewBox="0 0 10 10" aria-hidden="true"><path d="M0.5 2 H9.5 V8.5 H0.5 Z M1.2 2.6 L5 5.6 L8.8 2.6 Z" fill-rule="evenodd"/></svg>
      </li>
      <li>tolumo.com
        <svg viewBox="0 0 10 10" aria-hidden="true"><circle cx="5" cy="5" r="4.6"/></svg>
      </li>
    </ul>
    <div class="brand"><span class="brand-dot"></span>tolumo</div>
    <div class="divider"></div>
    <p class="services">Aerial Visual for Real Estate | Insurance | Construction | Film</p>
    <p class="certification">KTO Part 107 Commercial sUAS Certified attached..,</p>
  </section>
  <section class="card card-back">
    <div class="brand"><span class="brand-dot"></span>tolumo</div>
  </section>
</main>
</body>
</html>
```